Torvane Facilities Business Card Design

We would now like to design business cards with the new Torvane Facilities logo

Target Market(s)

Professional

Industry/Entity Type

Professional services

Contact Information for Business Card

Employee name, title, phone number, email address, corporate office address and logo.

Font styles to use
Sans Serif

Colors
0054AA
0677BA
7BADD7
CADEEF
E8F1F8

Requirements
Must have
• My logo
Should not have
• any other pictures or images besides my logo

```html
<!DOCTYPE html>
<html lang="en">
<head>
<meta charset="UTF-8">
<title>Torvane Facilities Business Card</title>
<link href="https://fonts.googleapis.com/css2?family=Open+Sans:wght@400;600;700&display=swap" rel="stylesheet">
<style>
  :root {
    --navy: #0054AA;
    --blue: #0677BA;
    --sky: #7BADD7;
    --mist: #CADEEF;
    --ice: #E8F1F8;
    --ink: #5a5a5a;
    --paper: #ffffff;
    --stage: #2b2b2b;
  }
  * { margin: 0; padding: 0; box-sizing: border-box; }
  html, body { width: 1200px; height: 900px; overflow: hidden; }
  body {
    background: var(--stage);
    font-family: "Open Sans", Arial, sans-serif;
    position: relative;
  }
  .card {
    position: absolute;
    width: 600px;
    height: 343px;
    background: var(--paper);
    overflow: hidden;
    box-shadow: 0 12px 30px rgba(0,0,0,.45);
  }

  /* Shared brand lockup */
  .brand {
    display: flex; align-items: center; gap: 12px;
    color: var(--blue); font-weight: 700; line-height: 1;
    white-space: nowrap;
  }
  .brand__mark { background: var(--blue); flex: none; }

  /* Back side */
  .card--back { left: 90px; top: 70px; }
  .card--back .texture {
    position: absolute; inset: 0;
    background: linear-gradient(135deg, #f8f8f8 0%, #ececec 100%);
  }
  .card--back .brand-wrap {
    position: absolute; inset: 0;
    display: flex; align-items: center; justify-content: center;
  }
  .card--back .brand { font-size: 32px; gap: 14px; }
  .card--back .brand__mark { width: 32px; height: 32px; }

  /* Front side */
  .card--front { left: 510px; top: 487px; }
  .card--front .accent-field { position: absolute; inset: 0; }
  .card--front .brand {
    position: absolute; left: 36px; top: 44px;
    font-size: 24px;
  }
  .card--front .brand__mark { width: 26px; height: 26px; }
  .holder {
    position: absolute; left: 36px; top: 172px;
  }
  .holder__name {
    color: var(--blue); font-weight: 700; font-size: 17px; letter-spacing: .3px;
    white-space: nowrap;
  }
  .holder__title { color: var(--ink); font-size: 13px; margin-top: -2px; }
  .contacts {
    position: absolute; left: 36px; top: 238px;
    color: var(--ink); font-size: 12.5px;
    display: grid; grid-template-columns: auto auto; column-gap: 26px; row-gap: 5px;
  }
  .contact { display: flex; align-items: center; gap: 8px; white-space: nowrap; }
  .contact--wide { grid-column: 1 / 3; }
  .contact svg { width: 13px; height: 13px; fill: var(--blue); flex: none; }
</style>
</head>
<body>

  <section class="card card--back">
    <div class="texture" role="img" aria-label="Faint repeating brand pattern across the card"></div>
    <div class="brand-wrap">
      <div class="brand"><span class="brand__mark"></span><span>Torvane Facilities</span></div>
    </div>
  </section>

  <section class="card card--front">
    <svg class="accent-field" width="600" height="343" viewBox="0 0 600 343">
      <polygon points="400,0 600,0 600,265 375,180" fill="#CADEEF" role="img" aria-label="Light blue repeating brand pattern panel"/>
      <line x1="178" y1="182" x2="375" y2="180" stroke="#0677BA" stroke-width="1.2"/>
    </svg>

    <div class="brand"><span class="brand__mark"></span><span>Torvane Facilities</span></div>

    <div class="holder">
      <div class="holder__name">DANIEL REEVE</div>
      <div class="holder__title">Director</div>
    </div>

    <div class="contacts">
      <div class="contact contact--wide">
        <svg viewBox="0 0 24 24"><path d="M6.6 10.8a15 15 0 0 0 6.6 6.6l2.2-2.2a1 1 0 0 1 1-.25 11.4 11.4 0 0 0 3.6.6 1 1 0 0 1 1 1V20a1 1 0 0 1-1 1A17 17 0 0 1 3 4a1 1 0 0 1 1-1h3.5a1 1 0 0 1 1 1c0 1.25.2 2.45.6 3.6a1 1 0 0 1-.25 1z"/></svg>
        <span>0614 208 375</span>
      </div>
      <div class="contact">
        <svg viewBox="0 0 24 24"><path d="M2 5h20v14H2z M2 5l10 8 10-8" fill="none" stroke="#0677BA" stroke-width="2.4"/></svg>
        <span>info@TorvaneFacilities.com</span>
      </div>
      <div class="contact">
        <svg viewBox="0 0 24 24"><circle cx="12" cy="12" r="10"/><path d="M2 12h20M12 2c3 3 3 17 0 20M12 2c-3 3-3 17 0 20" stroke="#fff" stroke-width="1.4" fill="none"/></svg>
        <span>www.TorvaneFacilities.com</span>
      </div>
      <div class="contact contact--wide">
        <svg viewBox="0 0 24 24"><path d="M12 2a7 7 0 0 0-7 7c0 5 7 13 7 13s7-8 7-13a7 7 0 0 0-7-7zm0 9.5A2.5 2.5 0 1 1 12 6.5a2.5 2.5 0 0 1 0 5z"/></svg>
        <span>24 Harrow Lane, Eastbridge, P.O Box 1180 Westmere</span>
      </div>
    </div>
  </section>

</body>
</html>
```